Commercial and Multifamily informational website

We need a website for our commercial real estate management company. We will manage offices, retail, apartments and others. Here is the brief verbiage: Providing quality commercial and multifamily portfolio management to Landlords, REITs, and financial institutions. 

Industry/Entity Type

Real Estate

Number of Pages Required

2 page

Font styles to use
Sans Serif
Other font styles liked:
• Muli, Garamond

Colors
0555a3
5c5c5c
3176b5
85acd3
474747

Requirements
Must have
• Home page and contact page

```html
<!DOCTYPE html>
<html lang="en">
<head>
<meta charset="utf-8">
<title>Halvern Real Estate Management</title>
<link href="https://fonts.googleapis.com/css2?family=Mulish:wght@400;600;700;800&family=Open+Sans:wght@400;600;700&display=swap" rel="stylesheet">
<style>
:root{
  --navy:#1d3a82;
  --navy-dark:#17306e;
  --navy-mid:#24438f;
  --blue:#0555a3;
  --accent:#3176b5;
  --light-blue:#85acd3;
  --text:#5c5c5c;
  --dark:#474747;
  --ink:#1b1b1b;
  --grey-bar:#ececec;
  --grey-bg:#e9e9e9;
}
*{box-sizing:border-box;margin:0;padding:0}
html,body{width:1200px;height:3291px;overflow:hidden}
body{position:relative;font-family:"Open Sans",sans-serif;color:var(--text);background:#fff}
section,header,nav,footer,.topbar,.bottombar{position:absolute;left:0;width:1200px}

.topbar{top:0;height:33px;background:var(--grey-bar);font-size:13px;color:#6a6a6a;display:flex;justify-content:space-between;align-items:center;padding:0 80px}

.site-header{top:33px;height:92px;background:#fff;display:flex;align-items:center;padding:0 80px}
.brand{display:flex;align-items:center;gap:14px}
.brand-mark{width:34px;height:34px;background:var(--navy)}
.brand-name{font-family:"Mulish",sans-serif;font-weight:700;color:var(--navy);font-size:18px;line-height:20px;text-transform:uppercase}
.contact-strip{margin-left:auto;display:flex;gap:64px}
.contact-item{display:flex;gap:12px;align-items:flex-start;font-size:14px;line-height:18px;color:#555}
.contact-item strong{display:block;color:var(--ink);font-weight:700}

.main-nav{top:125px;height:48px;background:var(--navy)}
.main-nav ul{list-style:none;display:flex;height:100%;padding-left:80px}
.main-nav li{height:100%;display:flex;align-items:center;padding:0 28px;font-size:13px;color:#fff;text-transform:uppercase}
.main-nav li.active{background:#4a4a4a}

.hero{top:173px;height:545px;background:
  linear-gradient(90deg,rgba(0,0,0,0) 0%,rgba(0,0,0,0) 70%,rgba(150,70,25,.55) 76%,rgba(110,55,25,.85) 86%,rgba(70,40,22,.9) 100%),
  linear-gradient(180deg,#e9b35f 0%,#d99b4b 22%,#b9864d 38%,#8d8a80 48%,#5e6a63 56%,#6f6a55 64%,#4b4a44 76%,#3a332e 100%)}
.hero-content{position:absolute;left:78px;top:128px;width:700px;color:var(--ink)}
.hero h1{font-family:"Mulish",sans-serif;font-weight:400;font-size:32px;line-height:38px}
.hero h1 span{display:block;font-weight:800;font-size:44px;line-height:56px;color:var(--navy);white-space:nowrap}
.hero p{font-size:13.5px;line-height:22px;margin-top:8px;color:#222;width:540px}
.btn-dark{display:inline-block;margin-top:24px;background:#3f3f3f;color:#fff;font-size:13px;padding:12px 33px;text-transform:uppercase;border-radius:3px}

.services{top:718px;height:583px}
.services-visual{position:absolute;left:86px;top:83px;width:410px;height:410px}
.visual-room{position:absolute;left:0;top:0;width:354px;height:257px;background:
  linear-gradient(180deg,#5a564f 0%,#8f887c 18%,#e6e1d6 38%,#f2eee6 55%,#b9ad9a 72%,#5b4a3a 100%)}
.visual-frame{position:absolute;left:22px;top:20px;width:332px;height:226px;border:3px solid #fff}
.visual-worker{position:absolute;left:189px;top:220px;width:222px;height:190px;background:
  radial-gradient(ellipse 30% 45% at 45% 60%,#e0782a 0%,rgba(224,120,42,0) 100%),
  linear-gradient(180deg,#a9c3de 0%,#c8d6e3 45%,#7f8a8f 75%,#4c5052 100%);border:3px solid #fff}
.services-text{position:absolute;left:551px;top:90px;width:540px}
.section-title{font-family:"Mulish",sans-serif;font-weight:800;font-size:26px;color:var(--ink);display:flex;align-items:center;gap:12px;letter-spacing:.3px;text-transform:uppercase}
.section-title .bar{width:5px;height:24px;background:var(--light-blue)}
.services-text p{font-size:13.5px;line-height:24px;margin-top:18px;color:#555}
.btn-outline{display:inline-block;margin-top:26px;border:2px solid var(--navy);color:var(--navy);font-size:13px;padding:10px 32px;border-radius:4px;text-transform:uppercase;font-weight:600}

.management{top:1301px;height:340px;background:
  linear-gradient(90deg,rgba(255,255,255,.06),rgba(255,255,255,0) 40%,rgba(255,255,255,.08) 80%,rgba(255,255,255,0)),
  linear-gradient(180deg,#2c4c96,#1e3c85);text-align:center;color:#fff}
.management h2{font-family:"Mulish",sans-serif;font-weight:800;font-size:33px;margin-top:60px;display:inline-block;padding:8px 46px 10px;border-top:1px solid rgba(255,255,255,.35);border-bottom:1px solid rgba(255,255,255,.35);text-transform:uppercase}
.management p{font-size:14px;line-height:22px;width:1060px;margin:22px auto 0}
.management .btn-dark{margin-top:30px;padding:12px 46px}

.gallery{top:1641px;height:838px}
.gallery h2{font-family:"Mulish",sans-serif;font-weight:800;font-size:26px;text-align:center;color:var(--ink);margin-top:80px;text-transform:uppercase}
.gallery-grid{position:absolute;left:94px;top:162px;width:1014px;display:grid;grid-template-columns:repeat(5,187px);grid-auto-rows:187px;gap:19px 20px}
.tile{width:100%;height:100%}
.tile.wide{grid-column:span 2}
.t-garden{background:linear-gradient(180deg,#3f7fd0 0%,#7fb0e2 25%,#4f7a3e 42%,#e9ebea 52%,#c7c3bb 66%,#9c7a52 72%,#c9b9a0 100%)}
.t-drive{background:linear-gradient(180deg,#5a9be0 0%,#9cc4ea 28%,#f2f2f0 40%,#9a6a3e 55%,#d6d3cc 75%,#bdb8ae 100%)}
.t-terrace{background:linear-gradient(180deg,#2d6cc4 0%,#6ea1da 35%,#5d8c4c 55%,#e2e5e8 68%,#9aa0a4 100%)}
.t-glass{background:linear-gradient(180deg,#2e5fa8 0%,#9fb7d3 30%,#f0f0ee 42%,#3c4248 60%,#9ea3a6 85%,#d8d6d0 100%)}
.t-pool-terrace{background:linear-gradient(180deg,#3e7fd2 0%,#b7d2ec 35%,#eef0f1 48%,#8ab7cf 62%,#6b6761 80%,#3e3a36 100%)}
.t-dusk{background:linear-gradient(180deg,#1f4f9c 0%,#4a77b8 30%,#d9d4c8 45%,#3a3530 65%,#d6a35a 78%,#4a4038 100%)}
.t-pool{background:linear-gradient(180deg,#3a5430 0%,#5f8a48 30%,#e8e4dc 45%,#3fa7d6 62%,#7bc6e6 72%,#8b5a36 85%,#3a2a20 100%)}
.t-villa{background:linear-gradient(180deg,#8fa9c6 0%,#dfe4ea 25%,#f4f4f2 55%,#cfc9bf 75%,#a49e94 100%)}
.t-living{background:linear-gradient(180deg,#f4f4f2 0%,#e6e8ea 40%,#ffffff 58%,#c9b29a 72%,#8c4a26 100%)}
.t-bedroom{background:linear-gradient(180deg,#efeeea 0%,#d9d6ce 35%,#f7f6f3 60%,#a4603a 80%,#6e3520 100%)}
.t-kitchen{background:linear-gradient(180deg,#e8e6e2 0%,#6e6a64 30%,#d5d2cc 50%,#3d3935 70%,#7d5a3e 100%)}
.t-entry{background:linear-gradient(90deg,#2a2520 0%,#5a4434 18%,#b08a62 34%,#4a3a2e 48%,#6c8f5a 64%,#3a6e8a 82%,#2d5a78 100%)}

.testimonials{top:2534px;height:384px;background:var(--grey-bg)}
.testimonials .section-title{position:absolute;left:80px;top:43px}
.testimonial{position:absolute;top:121px;width:502px;height:186px;background:#fff}
.testimonial.one{left:83px}
.testimonial.two{left:617px}
.avatar{position:absolute;left:0;top:15px;width:152px;height:170px}
.avatar.warm{background:radial-gradient(ellipse 45% 50% at 50% 40%,#d9a98a 0%,rgba(217,169,138,0) 100%),linear-gradient(160deg,#f1e8e2 0%,#b88f77 55%,#5a2f84 100%)}
.avatar.cool{background:radial-gradient(ellipse 45% 50% at 50% 45%,#c49274 0%,rgba(196,146,116,0) 100%),linear-gradient(180deg,#9a9a9a 0%,#7e7e7e 60%,#5a5a5a 100%)}
.t-name{position:absolute;left:135px;top:25px;background:#4a4a4a;color:#fff;font-family:"Mulish",sans-serif;font-weight:700;font-size:14px;padding:7px 42px}
.t-quote{position:absolute;left:178px;top:78px;width:300px;font-size:13px;line-height:21px;color:#555}

.site-footer{top:2918px;height:336px;display:flex;color:#fff}
.footer-col{width:400px;height:100%;padding:40px 0 0 66px;background:var(--navy-dark)}
.footer-col.mid{background:var(--navy-mid);padding-left:31px}
.footer-col.right{padding-left:31px}
.footer-title{font-family:"Mulish",sans-serif;font-weight:800;font-size:16px;display:flex;align-items:center;gap:8px;text-transform:uppercase}
.footer-title .bar{width:5px;height:18px;background:var(--light-blue)}
.footer-brand{display:flex;align-items:center;gap:12px;margin-top:28px}
.footer-brand .brand-mark{background:#fff}
.footer-brand .brand-name{color:#fff}
.footer-col p{font-size:13px;line-height:19px;margin-top:14px;width:320px}
.social{display:flex;gap:4px;margin-top:36px}
.social span{width:17px;height:17px;background:#fff}
.news{display:flex;gap:14px;margin-top:26px}
.news-date{width:33px;height:42px;flex:none;background:#5b6a8e;text-align:center;font-family:"Mulish",sans-serif;font-weight:800;font-size:15px;line-height:22px}
.news-date small{display:block;font-size:8px;line-height:10px;font-weight:600}
.news-date.plain{background:none}
.news p{margin:0;width:280px;font-size:13px;line-height:19px}
.news p span{color:#aab8d8}
.info{display:grid;grid-template-columns:93px 1fr;margin-top:26px;font-size:13px;line-height:19px}
.info dt,.info dd{padding-bottom:24px}
.info dd span{color:#aab8d8}

.bottombar{top:3254px;height:37px;background:#11265a;color:#fff;font-size:12px;display:flex;align-items:center;justify-content:space-between;padding:0 78px}
.bottombar ul{list-style:none;display:flex}
.bottombar li{padding:0 12px;border-left:1px solid #fff;line-height:12px;text-transform:uppercase}
.bottombar li:first-child{border-left:0}
</style>
</head>
<body>

<div class="topbar">
  <span>Halvern. We specialize in: Real Estate Management</span>
  <span>Wednesday, November 09, 2016 4:39:48 PM</span>
</div>

<header class="site-header">
  <div class="brand">
    <span class="brand-mark"></span>
    <span class="brand-name">Halvern<br>Real Estate<br>Management</span>
  </div>
  <div class="contact-strip">
    <div class="contact-item">
      <svg width="24" height="24" viewBox="0 0 24 24" fill="none" stroke="#7b8aa8" stroke-width="1.6"><path d="M5 3h4l2 5-2.5 1.5a11 11 0 0 0 6 6L16 13l5 2v4a2 2 0 0 1-2 2A17 17 0 0 1 3 5a2 2 0 0 1 2-2z"/></svg>
      <div><strong>555.010.5240</strong>info@halvern-rem.com</div>
    </div>
    <div class="contact-item">
      <svg width="22" height="26" viewBox="0 0 22 26" fill="none" stroke="#7b8aa8" stroke-width="1.6"><path d="M11 25s8-8 8-14a8 8 0 0 0-16 0c0 6 8 14 8 14z"/><circle cx="11" cy="11" r="3"/></svg>
      <div><strong>120 Harbor Lane</strong>Eastport, NY 10020</div>
    </div>
  </div>
</header>

<nav class="main-nav">
  <ul>
    <li class="active">Home</li><li>About Us</li><li>Services</li><li>Image Gallery</li><li>Testimonails</li><li>Clients</li><li>Contact Us</li>
  </ul>
</nav>

<section class="hero" role="img" aria-label="Sunset view from a balcony with glass windows over a lakeside residential neighbourhood">
  <div class="hero-content">
    <h1>Our Commercial Real Estate <span>MANAGEMENT HALVERN</span></h1>
    <p>simply dummy text of the printing and typesetting industry. Lorem Ipsum has been the industry's standard dummy text ever since the 1500s.</p>
    <span class="btn-dark">More Details</span>
  </div>
</section>

<section class="services">
  <div class="services-visual">
    <div class="visual-room" role="img" aria-label="Bright living room with a white sectional sofa"></div>
    <div class="visual-frame"></div>
    <div class="visual-worker" role="img" aria-label="Construction supervisor in safety vest on a building site"></div>
  </div>
  <div class="services-text">
    <h2 class="section-title"><span class="bar"></span>Services Offered</h2>
    <p>Halvern will take you through each step of your project, including design, cost, finance, and construction, from the biggest to the smallest of details. Our 'pro-active' approach and responsiveness to our client's needs reassures them that Halvern is the right choice!</p>
    <p>Halvern can take your project from the earliest stage to final completion. We can perform site/space analysis (from a construction point of view), budget analysis, help with office layout/design, and value engineering. This important, early groundwork will set the stages for the project of your dreams blending the right time constraints, quality level and cost to suit your specific needs.</p>
    <p>Real Estate Management manages their team of professionals to provide an outstanding result every time.</p>
    <span class="btn-outline">More Details</span>
  </div>
</section>

<section class="management">
  <h2>Real Estate Management</h2>
  <p>We are a niche construction firm focusing on medical office fit out , remodeling and construction for medical professionals. We service the Westchester and Putnam N.Y. counties as well as all of Fairfield county, CT. With over 14 years of experience we can make the process more stream lined and less distracting to the doctors we are working for, allowing them to stay focused on their practice.</p>
  <span class="btn-dark">Get a Touch</span>
</section>

<section class="gallery">
  <h2>Our Gallery</h2>
  <div class="gallery-grid">
    <div class="tile wide t-garden" role="img" aria-label="Modern white house with palm garden"></div>
    <div class="tile t-drive" role="img" aria-label="Driveway and timber facade"></div>
    <div class="tile t-terrace" role="img" aria-label="Rooftop terrace with glass railing"></div>
    <div class="tile t-glass" role="img" aria-label="Glass walled modern home"></div>
    <div class="tile t-pool-terrace" role="img" aria-label="Poolside terrace under blue sky"></div>
    <div class="tile t-dusk" role="img" aria-label="House exterior lit at dusk"></div>
    <div class="tile wide t-pool" role="img" aria-label="Backyard swimming pool with deck"></div>
    <div class="tile t-villa" role="img" aria-label="White villa with patio"></div>
    <div class="tile t-living" role="img" aria-label="Living room with white sofas"></div>
    <div class="tile t-bedroom" role="img" aria-label="Bedroom with ceiling fan"></div>
    <div class="tile t-kitchen" role="img" aria-label="Modern kitchen"></div>
    <div class="tile wide t-entry" role="img" aria-label="Entrance hallway opening to garden"></div>
  </div>
</section>

<section class="testimonials">
  <h2 class="section-title"><span class="bar"></span>Testimonials</h2>
  <div class="testimonial one">
    <div class="avatar warm" role="img" aria-label="Portrait of a client"></div>
    <div class="t-name">Dana Whitmore</div>
    <p class="t-quote">They are experts at the medical/dental office build-out, and I maintained full confidence in their work."</p>
  </div>
  <div class="testimonial two">
    <div class="avatar cool" role="img" aria-label="Portrait of a client"></div>
    <div class="t-name">Owen R Castell</div>
    <p class="t-quote">Lorem ipsum dolor sit amet, consectetur cing elit, sed do eiusmod tempor incididunt labore et dolore magna aliqua ...</p>
  </div>
</section>

<footer class="site-footer">
  <div class="footer-col">
    <h3 class="footer-title"><span class="bar"></span>About Us</h3>
    <div class="footer-brand">
      <span class="brand-mark"></span>
      <span class="brand-name">Halvern<br>Real Estate<br>Management</span>
    </div>
    <p>Lorem ipsum dolor sit amet, consectetuer adiscing elit, sed diam nonummy nibh euismod tincidunt laoreet dolore magna aliquam.</p>
    <div class="social"><span></span><span></span><span></span><span></span><span></span></div>
  </div>
  <div class="footer-col mid">
    <h3 class="footer-title"><span class="bar"></span>News Update</h3>
    <div class="news">
      <div class="news-date">04<small>Feb</small></div>
      <p>Claritas est etiam processus dynamicus, qui sequitur mutationem consuetudium<br><span>26 Comments</span></p>
    </div>
    <div class="news">
      <div class="news-date plain">04<small>Feb</small></div>
      <p>Claritas est etiam processus dynamicus, qui sequitur mutationem consuetudium<br>26 Comments</p>
    </div>
  </div>
  <div class="footer-col right">
    <h3 class="footer-title"><span class="bar"></span>Get In Touch</h3>
    <dl class="info">
      <dt>Address:</dt><dd>42 Linden Court, Suite 6<br>Millbrook, CA 94100</dd>
      <dt>Phone:</dt><dd>555.014.8860 - Tel<br>555.010.5240 - Cell</dd>
      <dt>Email:</dt><dd><span>support@halvern-rem.com</span><br><span>info@halvern-rem.com</span></dd>
    </dl>
  </div>
</footer>

<div class="bottombar">
  <span>© 2016 | Copyright .All Rights Reserved</span>
  <ul><li>Home</li><li>About Us</li><li>Services</li><li>Image Gallery</li><li>Testimonails</li><li>Clients</li><li>Contact Us</li></ul>
</div>

</body>
</html>
```